cover arrangement / layout for "The Lantern Shelf Habit"

I want a cover layout (one for e-book, one for paperback) that is professional enough to compete with the likes of the Rolf Whitcombe, Dorian Pelk, Everett Castlemoor and Hugo Varnel's of the world. I have the book title logo, font, and color pallette - but I want some ideas for the cover (front cover only) layout.

I'm attaching the logo (white on transparent background), as well as the "sample" cover I've been using in mockups. I'm not looking for revolutionary designs or new logos, but rather a "cover" (the whole thing) design and arrangement.

Here are the parameters for the cover designs:

• eBook: 1600 x 2560 pixels, 72 ppi, RGB colorspace

• Physical book: 8.5 x 5.5 inches, 300 ppi, CMYK colorspace

For the physical book, if the designers don't extend the artwork to go outside the entire book, no bleeds need to be added.

We'll need the following from the winning designer(s):

1. An editable source file of the cover design, with open layers (AI; PSD); and

2. The fonts used. My brand fonts are Zing Rust Base, and Overpass. Those should be used, however I'm also open to alternative ideas as an additional consideration.

```html
<!DOCTYPE html>
<html lang="en">
<head>
<meta charset="utf-8">
<title>The Lantern Shelf Habit — Front Cover</title>
<link href="https://fonts.googleapis.com/css2?family=Bebas+Neue&family=Anton&family=Overpass:wght@400&display=swap" rel="stylesheet">
<style>
  :root {
    --backdrop: #e6e6e4;
    --cover-paper: #ffffff;
    --title-rust: #c8593f;
    --author-ink: #141414;
    --subtitle-ink: #1c1c1c;
    --jar-glass: #c9ccca;
    --jar-coins: #8a6a4f;
  }
  * { margin: 0; padding: 0; box-sizing: border-box; }
  html, body {
    width: 1200px;
    height: 1080px;
    overflow: hidden;
    background: var(--backdrop);
  }
  .stage {
    position: relative;
    width: 1200px;
    height: 1080px;
    display: flex;
    align-items: center;
    justify-content: center;
  }
  .cover {
    position: relative;
    width: 640px;
    height: 990px;
    background: var(--cover-paper);
    box-shadow: 0 6px 24px rgba(0, 0, 0, 0.12);
    display: flex;
    flex-direction: column;
    align-items: center;
  }
  .cover-title {
    margin-top: 52px;
    font-family: "Bebas Neue", "Oswald", sans-serif;
    font-weight: 400;
    color: var(--title-rust);
    font-size: 136px;
    line-height: 114px;
    text-align: center;
    letter-spacing: 1px;
    text-transform: uppercase;
  }
  .cover-title span { display: block; white-space: nowrap; }
  .cover-art {
    position: relative;
    width: 200px;
    height: 150px;
    margin-top: 14px;
  }
  .cover-art .jar {
    position: absolute;
    left: 50%;
    top: 0;
    width: 100px;
    height: 132px;
    transform: translateX(-50%);
    border-radius: 16px 16px 12px 12px;
    background: linear-gradient(180deg, var(--jar-glass) 0%, var(--jar-coins) 55%, #6e5440 100%);
  }
  .cover-art .coins {
    position: absolute;
    left: 0;
    bottom: 0;
    width: 200px;
    height: 28px;
    border-radius: 50%;
    background: radial-gradient(ellipse at center, var(--jar-coins) 0%, rgba(138, 106, 79, 0.4) 70%, rgba(138, 106, 79, 0) 100%);
  }
  .cover-author {
    margin-top: 12px;
    font-family: "Anton", "Oswald", sans-serif;
    font-weight: 400;
    color: var(--author-ink);
    font-size: 80px;
    line-height: 88px;
    text-align: center;
    text-transform: uppercase;
  }
  .cover-author span { display: block; white-space: nowrap; }
  .cover-subtitle {
    margin-top: 22px;
    font-family: "Overpass", "Helvetica Neue", sans-serif;
    font-weight: 400;
    color: var(--subtitle-ink);
    font-size: 19px;
    line-height: 22px;
    letter-spacing: 1.5px;
    text-align: center;
    text-transform: uppercase;
  }
</style>
</head>
<body>
  <main class="stage">
    <section class="cover">
      <h1 class="cover-title">
        <span>The</span>
        <span>Lantern</span>
        <span>Shelf</span>
        <span>Habit</span>
      </h1>
      <div class="cover-art" role="img" aria-label="Glass jar filled with coins, more coins spilled around its base">
        <div class="coins"></div>
        <div class="jar"></div>
      </div>
      <p class="cover-author">
        <span>Marcus</span>
        <span>Tellbridge Jr</span>
      </p>
      <p class="cover-subtitle">How to re-engage and reignite<br>your workforce</p>
    </section>
  </main>
</body>
</html>
```